Design eBook cover and interior pages for vegan investment consulting firm and membership service...

I have completed an eBook that is about 6 pages of printed text (see attached PDF). I am seeking a cover page and a cool design for the interior pages. The final product should be as concise as possible while being easy to read, and not to exceed 10 pages total in any case.

My business is named Plantwise Harbor. You can learn more about the company by visiting https://plantwiseharbor.example. There, you’ll also see our current color and design choices.

We are about to start a Phase II redesign of the website, so it is not required that you match the color and style of our website. I am open to any fresh ideas regarding color, fonts, and overall aesthetic that might also inform our website redesign.

The business serves individuals “investor members” who have $50,000 or more in their investment portfolio, and also provides “purpose driven” portfolio design consulting to endowments, large asset managers, and high net worth individuals who are looking to build a vegan portfolio over $10 million or more.

Because we’re dealing with investing and people’s life savings, we want the eBook look to convey responsibility and integrity. At the same time, our audience will participate because of they are also passionate about all things vegan - protecting animals, the environment, and human health. To summarize, the goal is to have an eBook design that conveys a blend of responsibility, integrity, and passion.

Note - there is a tendency for people to first think of the color green when designing for vegan enterprises. I feel that using green as a major and even as a minor color often creates difficult or weak design outcomes. Green has become a kind of design shorthand for all things vegan and environmental, and as a result, I feel it has lost any special meaning.

Since we provide serious services to people who take investing seriously, I want color and design styles that read well, and convey responsibility, integrity and passion without relying on overused design cliches, but while still conveying a fresh perspective.

```html
<!DOCTYPE html>
<html lang="en">
<head>
<meta charset="utf-8">
<title>Meet Daniel Hartwell</title>
<link rel="stylesheet" href="https://fonts.googleapis.com/css2?family=Open+Sans:wght@400;600&family=Roboto:wght@300;400&display=swap">
<style>
  :root {
    --paper: #ffffff;
    --ink: #1f1f1f;
    --accent: #a01c2a;
    --rule-dark: #3a3a3a;
    --photo-top: #6b4a36;
    --photo-bottom: #b9c4c8;
    --signature-tint: #e6ecf5;
  }
  html, body {
    margin: 0;
    padding: 0;
    width: 927px;
    height: 1200px;
    overflow: hidden;
    background: var(--paper);
  }
  .page {
    position: relative;
    width: 927px;
    height: 1200px;
    background: var(--paper);
    color: var(--ink);
  }
  .page-title {
    position: absolute;
    left: 85px;
    top: 100px;
    margin: 0;
    font-family: "Roboto", sans-serif;
    font-weight: 300;
    font-size: 26px;
    color: var(--accent);
    letter-spacing: 0.1px;
  }
  .title-rule {
    position: absolute;
    left: 85px;
    top: 137px;
    width: 756px;
    height: 1px;
    background: var(--accent);
  }
  .portrait {
    position: absolute;
    left: 85px;
    top: 221px;
    width: 188px;
    height: 239px;
    background: linear-gradient(180deg, var(--photo-top) 0%, #8a6a58 45%, var(--photo-bottom) 100%);
  }
  .portrait-caption {
    position: absolute;
    left: 85px;
    top: 465px;
    width: 188px;
    margin: 0;
    text-align: center;
    font-family: "Roboto", sans-serif;
    font-size: 14.5px;
    color: var(--ink);
  }
  .letter {
    position: absolute;
    left: 343px;
    top: 210px;
    width: 498px;
    font-family: "Open Sans", sans-serif;
    font-size: 14.6px;
    line-height: 25.8px;
    color: var(--ink);
  }
  .letter p {
    margin: 0;
    text-align: justify;
    text-indent: 26px;
  }
  .letter p.lead {
    text-indent: 0;
  }
  .letter .closing {
    text-indent: 0;
    margin-top: 24px;
  }
  .signature {
    position: absolute;
    left: 343px;
    top: 1000px;
    width: 214px;
    height: 62px;
    background: var(--signature-tint);
  }
  .footer-rule {
    position: absolute;
    left: 85px;
    top: 1121px;
    width: 756px;
    height: 1px;
    background: var(--rule-dark);
  }
  .footer {
    position: absolute;
    left: 85px;
    top: 1128px;
    width: 756px;
    margin: 0;
    text-align: center;
    font-family: "Open Sans", sans-serif;
    font-size: 14.6px;
    letter-spacing: 0.3px;
    color: var(--ink);
  }
</style>
</head>
<body>
<main class="page">
  <h1 class="page-title">Meet Daniel Hartwell</h1>
  <div class="title-rule"></div>

  <div class="portrait" role="img" aria-label="Portrait photograph of the founder"></div>
  <p class="portrait-caption">Founder, Plantwise Harbor</p>

  <section class="letter">
    <p class="lead">Throughout my adult life, I have worked to solve difficult ecological, social, and health challenges with creative business, financial, and social organizing strategies.</p>
    <p>I started my first “purpose driven” environmental business in 1983, and by 1990 became one of the youngest environmental NGO directors in Washington, DC.</p>
    <p>These experiences solidified my belief that purpose driven businesses can be built to solve big challenges in ways that are not possible via charities, NGO’s, and governments alone.</p>
    <p>Not only are purpose driven businesses ideally suited to today’s challenges, it is clear to me that they can and should be highly profitable due to the vast and profitable market opportunities available for transforming our economy.</p>
    <p>To fulfill this vision, I had to learn one of the most challenging and misunderstood fields in the world corporate finance. In 2001, I left direct entrepreneurship and leadership to gain the financial experience needed to design, fund and grow purpose driven business at a rapid pace.</p>
    <p>Plantwise Harbor is the result of a lifetime of intense effort, wild stories, and my personal transformation from omnivore to vegan. As a community of investors sharing our passion for a vegan future, we can help fund existing vegan entrepreneurs and also design and finance vegan business projects from scratch to fill a wide range of overlooked market opportunities to make the world a better place for ourselves and our children.</p>
    <p>As the Plantwise Harbor community grows, investor members will have increasing opportunities to work together and grow the vegan economy for the benefit of the animals, human health, and the environment. I look forward to sharing this journey with you!</p>
    <p class="closing">Sincerely,</p>
  </section>

  <div class="signature" role="img" aria-label="Handwritten signature of the founder"></div>

  <div class="footer-rule"></div>
  <p class="footer">5 VEGAN BUSINESSES YOU SHOULD BE INVESTING IN TODAY | Page iii</p>
</main>
</body>
</html>
```